Visitenkarten-Design für Versicherungsmakler
Zielgruppe
Wir sind ein Versicherungsmakler aus Leipzig.
Aufgabenstellung
Im Anhang finden Sie die alte Visitenkarte. Die Daten können übernommen werden. Aber statt Inhaber bitte 'Geschäftsführer'
Die Farben sollten beibehalten werden. Bei der Frage ob das rot oder das grau die Primärfarbe ist, bin ich flexibel. Von der Gestaltung her sind Ihnen ansonsten keine Grenzen gesetzt.

```html
<!DOCTYPE html>
<html lang="de">
<head>
<meta charset="utf-8">
<title>Visitenkarten – verano Finance Consulting</title>
<link href="https://fonts.googleapis.com/css2?family=Open+Sans:wght@400;600;700&family=Montserrat:wght@500;600&display=swap" rel="stylesheet">
<style>
  :root {
    --brand-red: #cc161c;
    --brand-grey: #b5b5b5;
    --ink: #1d1d1d;
    --ink-soft: #444;
    --paper: #ffffff;
    --stage: #e9e9e9;
  }
  * { box-sizing: border-box; margin: 0; padding: 0; }
  html, body { width: 1200px; height: 900px; overflow: hidden; }
  body {
    background: var(--stage);
    font-family: "Open Sans", Arial, sans-serif;
    display: flex; align-items: center; justify-content: center; gap: 40px;
  }
  .card {
    position: relative; width: 540px; height: 340px;
    box-shadow: 0 6px 20px rgba(0,0,0,.18);
    overflow: hidden;
  }
  /* Front */
  .card--front { background: var(--paper); color: var(--ink); }
  .person { position: absolute; left: 40px; top: 36px; }
  .person__name { color: var(--brand-red); font-weight: 700; font-size: 23px; }
  .person__role { font-size: 14px; color: var(--ink-soft); margin-top: 2px; }
  .brand { position: absolute; text-align: center; }
  .brand__name {
    font-family: "Open Sans", Arial, sans-serif; font-weight: 600;
    font-size: 58px; line-height: 1; letter-spacing: 2px;
  }
  .brand__tag {
    font-family: "Montserrat", Arial, sans-serif; font-weight: 500;
    font-size: 17px; letter-spacing: 2.5px; margin-top: 6px;
  }
  .card--front .brand { right: 40px; top: 92px; width: 280px; }
  .card--front .brand__name { color: var(--brand-red); }
  .card--front .brand__tag { color: #555; }
  .contacts { position: absolute; left: 40px; top: 178px; list-style: none; font-size: 15px; }
  .contacts li { display: flex; align-items: center; gap: 10px; line-height: 22px; }
  .contacts svg { width: 15px; height: 15px; fill: var(--brand-red); flex: none; }
  .address { position: absolute; right: 48px; top: 236px; text-align: right; font-size: 16px; line-height: 22px; }
  .footer-band { position: absolute; left: 0; right: 0; bottom: 0; height: 30px; }
  .footer-band svg { position: absolute; inset: 0; width: 100%; height: 100%; }
  .footer-band__url {
    position: absolute; right: 40px; bottom: 5px; color: var(--paper);
    font-size: 15px; letter-spacing: 1.5px;
  }
  /* Back */
  .card--back { background: var(--brand-red); color: var(--paper); }
  .card--back .brand { left: 0; right: 0; top: 92px; }
  .card--back .brand__name { font-size: 72px; }
  .card--back .brand__tag { font-size: 21px; letter-spacing: 3px; }
  .legal {
    position: absolute; left: 20px; right: 20px; bottom: 28px;
    text-align: center; font-size: 11px; line-height: 16px;
  }
</style>
</head>
<body>
  <section class="card card--front" aria-label="Vorderseite">
    <div class="person">
      <div class="person__name">Lena Hartwig</div>
      <div class="person__role">Geschäftsführer</div>
    </div>
    <div class="brand">
      <div class="brand__name">verano</div>
      <div class="brand__tag">FINANCE CONSULTING</div>
    </div>
    <ul class="contacts">
      <li><svg viewBox="0 0 16 16" aria-hidden="true"><path d="M3 1l3 3-1.5 2a9 9 0 005.5 5.5L12 10l3 3-2 2C7 15 1 9 1 3z"/></svg>0341-48217306</li>
      <li><svg viewBox="0 0 16 16" aria-hidden="true"><path d="M4 0h8v16H4zM5.5 2v10h5V2zM7 13.5h2v1H7z" fill-rule="evenodd"/></svg>0172-5840391</li>
      <li><svg viewBox="0 0 16 16" aria-hidden="true"><path d="M4 1h8v4H4zM1 6h14v7h-3v2H4v-2H1zM5 11v3h6v-3z" fill-rule="evenodd"/></svg>0341-48217399</li>
      <li><svg viewBox="0 0 16 16" aria-hidden="true"><path d="M1 3h14v10H1zM2 4l6 5 6-5v-.2H2z" fill-rule="evenodd"/></svg>lena.hartwig@verano-finanz.de</li>
    </ul>
    <address class="address" style="font-style:normal">Lindenauer Weg 48<br>04179 Leipzig</address>
    <div class="footer-band">
      <svg viewBox="0 0 540 30" preserveAspectRatio="none" aria-hidden="true">
        <polygon points="0,0 310,0 290,30 0,30" fill="var(--brand-grey)"/>
        <polygon points="318,0 540,0 540,30 298,30" fill="var(--brand-red)"/>
      </svg>
      <span class="footer-band__url">www.verano-finanz.de</span>
    </div>
  </section>

  <section class="card card--back" aria-label="Rückseite">
    <div class="brand">
      <div class="brand__name">verano</div>
      <div class="brand__tag">FINANCE CONSULTING</div>
    </div>
    <p class="legal">Freier Versicherungsmakler mit Erlaubnis nach § 34d Abs. 1 GewO<br>Erlaubnisbehörde: Kammer Leipzig, Marktstraße 12, 04109 Leipzig – Reg.-Nr. D-4KTR-M81QZ-27</p>
  </section>
</body>
</html>
```